Neu Online platform and Web design for Professional Car Trade. LORVANTIQ

Web design for Professional Car Trade. www.lorvantiq.example European car dealer, trader, import, premium and classic cars, Campervans and trucks. The online platform must be modern, clean and very classy. We are agents that advise and help import vehicles from Europe. DESCRIPTION: We are professionals of the Import of Vehicles in Europe that need an informative Web page of their services. Under the Lorvantiq brand We help people to find their ideal car in the European market, mainly Germany. Completely revised and with official guarantee. Service with personalized attention and advice to the client since he chooses his first vehicle, search and delivery. Key on hand. We are dedicated to advising, managing and importing vehicles from different countries of the European Union for clients from all over the country. Our company is at your service in everything related to Import of vehicles. If you need any clarification about our services or our way of working, you can contact us by email by sending it to the following address: Info@lorvantiq.example where we will assist you and give you all the necessary information and try to clear all your doubts. We have different services tailored and adapted to the needs of our customers. 100% professional and carefree service, tell us what car you want and we take care of everything. Help with documentation and calculation of taxes, registration tax, circulation, ITV, traffic. Budget without commitment, simulation of all costs and final prices in Spain. We speak the language in origin We have a qualified professional team for the valuation and documentation of the vehicles that are needed. Approvals, reforms, small cards, historical .. etc Website in German, English and Spanish Examples / Examples: https://www.trasvelmotor.example/ https: // www. ruzelpick.example.uk/brenta www.ruzelpick.example.de http://motvelora.example Info: http://www.ruedapress.example/practicos/comprar-coche-alemania http://www.vehitrasa.example/residencia. php http://importacionesolmedaz.example/cotizaciones.php
Reason: I have not received the expected designs I have not received more designs as expected
Target Market(s)
Sale of import and export vehicles for the Spanish and German automobile market.
Industry/Entity Type
Automotive
Logo Text
LORVANTIQ
Number of Pages Required
5+ page
Requirements
Nice to have
- I have some idea how in a background put a nice picture of some classic vehicle.

```html
<!DOCTYPE html>
<html lang="en">
<head>
<meta charset="utf-8">
<title>Lorvantiq – Professional Car Trade</title>
<link href="https://fonts.googleapis.com/css2?family=Montserrat:wght@500&family=Ubuntu:wght@400;500;700&family=Lato:wght@400;700&display=swap" rel="stylesheet">
<style>
:root{
  --red:#ee2b2e;
  --black:#000;
  --ink:#222;
  --grey:#e4e4e4;
  --card:#e2e2e2;
  --line:#d8d8d8;
  --white:#fff;
  --footer:#000;
  --bottom:#1a1a1a;
}
*{box-sizing:border-box;margin:0;padding:0}
html,body{width:742px;height:1200px;overflow:hidden;background:var(--white)}
body{position:relative;font-family:"Lato",sans-serif;color:var(--ink)}
.abs{position:absolute}

.site-header{left:0;top:0;width:742px;height:49px;background:var(--black)}
.brand{left:61px;top:10px;font-family:"Montserrat",sans-serif;font-weight:500;font-size:22px;color:var(--white);letter-spacing:.3px}
.main-nav{right:72px;top:19px;display:flex;gap:19px;font-family:"Ubuntu",sans-serif;font-size:9px;color:var(--white)}

.hero{left:0;top:49px;width:742px;height:281px;background:linear-gradient(90deg,#f4f4f4 0%,#e9eaec 30%,#c9ccd0 55%,#d8d9db 75%,#eeeeee 100%)}
.hero-dots{right:63px;top:299px;display:flex;gap:7px}
.hero-dots span{width:8px;height:8px;border-radius:50%;background:var(--white)}
.hero-dots span.on{background:var(--red)}

.quote{left:72px;top:73px;width:185px;height:226px;background:var(--red)}
.quote h2{height:30px;background:var(--black);color:var(--white);font-family:"Ubuntu",sans-serif;font-weight:400;font-size:17px;text-align:center;line-height:30px}
.quote .field{position:absolute;left:9px;width:165px;height:22px;background:var(--white);font-family:"Ubuntu",sans-serif;font-size:7.5px;color:#222;line-height:22px;padding:0 8px;display:flex;justify-content:space-between}
.quote .btn{position:absolute;left:46px;top:190px;width:92px;height:23px;background:var(--black);color:var(--white);font-family:"Ubuntu",sans-serif;font-size:11px;text-align:center;line-height:23px}

.section-title{left:0;width:742px;text-align:center;font-family:"Ubuntu",sans-serif;font-size:18px;color:#111}
.section-title b{font-weight:700}
.rule{left:357px;width:28px;height:1px;background:#bbb}
.lead{left:96px;width:550px;text-align:center;font-size:7.5px;line-height:16px;color:#333}

.pillar{top:450px;width:103px;height:103px;border-radius:50%;background:var(--grey);display:flex;flex-direction:column;align-items:center;justify-content:center;font-family:"Ubuntu",sans-serif;font-weight:500;font-size:11.5px;color:#222;text-align:center;line-height:16px}
.pillar svg{margin-bottom:4px}
.read-more{left:340px;top:576px;width:65px;height:21px;border:1.5px solid #111;font-family:"Ubuntu",sans-serif;font-weight:700;font-size:7px;text-align:center;line-height:18px}

.divider{left:62px;top:634px;width:620px;height:1px;background:var(--line)}
.arrow-btn{top:648px;width:22px;height:23px;background:#e6e6e6}
.services-sub{left:0;top:695px;width:742px;text-align:center;font-size:8px;color:#333}

.service{top:733px;width:147px;height:218px;background:var(--card);text-align:center}
.service.active{background:var(--red);color:var(--white)}
.service h3{margin-top:18px;height:30px;font-family:"Ubuntu",sans-serif;font-weight:500;font-size:8px;line-height:13px;padding:0 14px}
.service .badge{width:58px;height:58px;border-radius:50%;background:var(--white);margin:6px auto 0;display:flex;align-items:center;justify-content:center;box-shadow:0 0 0 2px rgba(0,0,0,.04)}
.service p{margin-top:10px;font-size:6.6px;line-height:12.8px;padding:0 8px;color:#444}
.service.active p{color:var(--white)}
.service .more{width:16px;height:16px;border-radius:50%;background:var(--white);margin:9px auto 0;display:flex;align-items:center;justify-content:center}
.service.active .more{background:#d91f22;border:2px solid #f35456}

.site-footer{left:0;top:970px;width:742px;height:203px;background:var(--footer);color:var(--white)}
.loop{left:165px;top:994px;font-family:"Ubuntu",sans-serif;font-size:15px;color:var(--white)}
.email{left:306px;top:994px;width:201px;height:21px;border-radius:11px;background:var(--white);font-size:7px;color:#555;line-height:21px;padding-left:13px}
.subscribe{left:511px;top:994px;width:68px;height:21px;border-radius:11px;background:var(--red);color:var(--white);font-family:"Ubuntu",sans-serif;font-weight:700;font-size:7px;text-align:center;line-height:21px}
.foot-rule{left:62px;top:1036px;width:620px;height:1px;background:#333}
.vrule{top:1054px;width:1px;height:107px;background:#333}
.foot-h{top:1058px;font-family:"Ubuntu",sans-serif;font-size:11px;color:var(--white)}
.foot-text{left:62px;top:1080px;width:166px;font-size:7px;line-height:12.7px;color:var(--white);text-align:justify}
.links{top:1080px;font-size:7px;line-height:16px;color:var(--white);list-style:none}
.social{top:1083px;width:28px;height:28px;border-radius:50%;border:1.5px solid var(--white)}
.bottom-bar{left:0;top:1173px;width:742px;height:27px;background:var(--bottom);color:#ccc;font-size:7.5px;text-align:center;line-height:27px}
</style>
</head>
<body>

<header class="abs site-header">
  <div class="abs brand">Lorvantiq</div>
  <nav class="abs main-nav"><span>Home</span><span>About Us</span><span>Services</span><span>Cars</span><span>Reviews</span><span>Tax Calculation</span><span>Support</span><span>Contact</span></nav>
</header>

<section class="abs hero" role="img" aria-label="Smiling car salesman in a white shirt holding out car keys in a showroom with parked cars"></section>
<div class="abs hero-dots"><span class="on"></span><span></span><span></span><span></span></div>

<form class="abs quote">
  <h2>Get a Quote</h2>
  <div class="field" style="top:40px">Car Type<span>⌄</span></div>
  <div class="field" style="top:70px">Car Model<span>⌄</span></div>
  <div class="field" style="top:100px">Country<span>⌄</span></div>
  <div class="field" style="top:130px">Vat Rate<span>%</span></div>
  <div class="field" style="top:159px">Amount</div>
  <div class="btn">Tax Calculator</div>
</form>

<h2 class="abs section-title" style="top:352px"><b>Welcome To</b> Lorvantiq</h2>
<div class="abs rule" style="top:384px"></div>
<p class="abs lead" style="top:393px">Sed ut perspiciatis unde omnis iste natus error sit voluptatem accusantium doloremque laudantium, totam rem aperiam, eaque ipsa quae ab illo inventore veritatis et quasi architecto beatae vitae dicta sunt explicabo. Nemo enim ipsam voluptatem quia voluptas sit aspernatur aut odit aut fugit, sed quia consequuntur magni dolores eos qui ratione voluptatem</p>

<div class="abs pillar" style="left:61px">
  <svg width="48" height="40" viewBox="0 0 48 40"><path d="M14 4h16l3 8h2v10H11V12h2z" fill="#111"/><rect x="16" y="6" width="12" height="6" fill="#e4e4e4"/><path d="M2 28h8l10 3h10l12-6 3 3-14 10H10l-8-3z" fill="#111"/></svg>car dealer</div>
<div class="abs pillar" style="left:190px">
  <svg width="44" height="38" viewBox="0 0 44 38"><path d="M2 14l10-10 8 6 6-4 8 4 8-2-4 14-14 14-8-4-10-8z" fill="#111"/><path d="M16 22l6 6M20 18l6 6M24 14l6 6" stroke="#e4e4e4" stroke-width="2"/></svg>trader</div>
<div class="abs pillar" style="left:319px">
  <svg width="48" height="30" viewBox="0 0 48 30"><path d="M8 4h24v18H8zM32 10h8l6 7v5H32z" fill="#111"/><circle cx="14" cy="24" r="4" fill="#111" stroke="#e4e4e4" stroke-width="1.5"/><circle cx="38" cy="24" r="4" fill="#111" stroke="#e4e4e4" stroke-width="1.5"/><path d="M0 8h6M2 13h6M0 18h6" stroke="#111" stroke-width="2"/></svg>import</div>
<div class="abs pillar" style="left:448px">
  <svg width="60" height="22" viewBox="0 0 60 22"><path d="M2 14c0-4 6-5 12-6l8-6h18l10 6c6 1 8 3 8 6v3H2z" fill="#111"/><circle cx="14" cy="17" r="4" fill="#111" stroke="#e4e4e4" stroke-width="1.5"/><circle cx="46" cy="17" r="4" fill="#111" stroke="#e4e4e4" stroke-width="1.5"/></svg>premium and<br>classic cars</div>
<div class="abs pillar" style="left:577px">
  <svg width="52" height="28" viewBox="0 0 52 28"><path d="M2 4h32l10 8 6 2v8H2z" fill="#111"/><circle cx="12" cy="22" r="4" fill="#111" stroke="#e4e4e4" stroke-width="1.5"/><circle cx="40" cy="22" r="4" fill="#111" stroke="#e4e4e4" stroke-width="1.5"/></svg>Campervans<br>and trucks</div>

<div class="abs read-more">READ MORE</div>

<div class="abs divider"></div>
<div class="abs arrow-btn" style="left:61px"><svg width="22" height="23"><path d="M13 7l-4 4.5 4 4.5" stroke="#444" fill="none" stroke-width="1.2"/></svg></div>
<div class="abs arrow-btn" style="left:658px"><svg width="22" height="23"><path d="M9 7l4 4.5-4 4.5" stroke="#444" fill="none" stroke-width="1.2"/></svg></div>
<h2 class="abs section-title" style="top:648px"><b>Our</b> Services</h2>
<div class="abs rule" style="top:681px"></div>
<p class="abs services-sub">We have different services to measure and adapted to the needs of our clients</p>

<article class="abs service active" style="left:62px">
  <h3>Help with paperwork and Tax Calculation</h3>
  <div class="badge"><svg width="34" height="34" viewBox="0 0 34 34" fill="none" stroke="#999" stroke-width="1.2"><rect x="5" y="5" width="20" height="26"/><rect x="11" y="2" width="8" height="5"/><path d="M9 13h12M9 18h10M9 23h8"/><circle cx="25" cy="23" r="6"/><path d="M22 23l2 2 4-4"/></svg></div>
  <p>Sed ut perspiciatis unde omnis iste natus error sit voluptatem accusantium doloremque laudantium, totam rem aperiam, eaque ipsa quae ab illo inventore veritatis et quasi fugit,</p>
  <div class="more"><svg width="8" height="6"><path d="M1 1l3 3 3-3" stroke="#fff" fill="none" stroke-width="1.2"/></svg></div>
</article>
<article class="abs service" style="left:220px">
  <h3>Tax registration</h3>
  <div class="badge"><svg width="30" height="30" viewBox="0 0 30 30" fill="none" stroke="#999" stroke-width="1.2"><path d="M6 24l2-7 14-14 5 5-14 14zM8 17l5 5M19 6l5 5"/></svg></div>
  <p>Sed ut perspiciatis unde omnis iste natus error sit voluptatem accusantium doloremque laudantium, totam rem aperiam, eaque ipsa quae ab illo inventore veritatis et quasi fugit,</p>
  <div class="more"><svg width="8" height="6"><path d="M1 1l3 3 3-3" stroke="#777" fill="none" stroke-width="1.2"/></svg></div>
</article>
<article class="abs service" style="left:378px">
  <h3>Circulation</h3>
  <div class="badge"><svg width="34" height="34" viewBox="0 0 34 34" fill="none" stroke="#999" stroke-width="1.2"><circle cx="17" cy="18" r="13"/><path d="M12 18l4 4 7-8M17 2v3"/></svg></div>
  <p>Sed ut perspiciatis unde omnis iste natus error sit voluptatem accusantium doloremque laudantium, totam rem aperiam, eaque ipsa quae ab illo inventore veritatis et quasi fugit,</p>
  <div class="more"><svg width="8" height="6"><path d="M1 1l3 3 3-3" stroke="#777" fill="none" stroke-width="1.2"/></svg></div>
</article>
<article class="abs service" style="left:536px">
  <h3>ITV</h3>
  <div class="badge"><svg width="26" height="30" viewBox="0 0 26 30" fill="none" stroke="#999" stroke-width="1.2"><rect x="3" y="2" width="20" height="26"/><rect x="6" y="5" width="14" height="5"/><path d="M6 14h14M6 18h14M6 22h14M10 13v12M13.5 13v12M17 13v12"/></svg></div>
  <p>Sed ut perspiciatis unde omnis iste natus error sit voluptatem accusantium doloremque laudantium, totam rem aperiam, eaque ipsa quae ab illo inventore veritatis et quasi fugit,</p>
  <div class="more"><svg width="8" height="6"><path d="M1 1l3 3 3-3" stroke="#777" fill="none" stroke-width="1.2"/></svg></div>
</article>

<footer class="abs site-footer"></footer>
<div class="abs loop">Stay in the loop...</div>
<div class="abs email">Enter Email id</div>
<div class="abs subscribe">SUBSCRIBE</div>
<div class="abs foot-rule"></div>
<div class="abs vrule" style="left:269px"></div>
<div class="abs vrule" style="left:502px"></div>

<h4 class="abs foot-h" style="left:62px">About Us</h4>
<p class="abs foot-text">Sed ut perspiciatis unde omnis iste natus error sit voluptatem accusantium doloremque laudantium, totam rem aperiam, eaque ipsa quae ab illo inventore veritatis et quasi architecto beatae vitae dicta sunt explicabo.</p>

<h4 class="abs foot-h" style="left:308px">Quick Links</h4>
<ul class="abs links" style="left:308px"><li>Home</li><li>About Us</li><li>Services</li><li>Cars</li></ul>
<ul class="abs links" style="left:394px"><li>Tax Calculation</li><li>Reviews</li><li>Support</li></ul>

<h4 class="abs foot-h" style="left:541px">Follow Us</h4>
<div class="abs social" style="left:541px" aria-label="Social profile"></div>
<div class="abs social" style="left:578px" aria-label="Social profile"></div>
<div class="abs social" style="left:616px" aria-label="Social profile"></div>
<div class="abs social" style="left:654px" aria-label="Social profile"></div>

<div class="abs bottom-bar">© 2017 &nbsp;|&nbsp; www.lorvantiq.example</div>

</body>
</html>
```